College Apartment Leasing Flyer

We need a post card/flyer design for a college apartment rental company called RV Stewardship Partners. We lease apartments to college students and would like a post card/flyer that appeal to college students, that are bright colors and eye catching. We would like pictures showcasing our properties with various amenities including big kitchens, living rooms with 50 inch flat screen TVs, large outdoor patios, large rooftop decks, private bathrooms, and much more. Granite countertops, hardwood floors, ceiling fans are some of the many amenities these apartments offer college students.

We want a flyer that advertises these apartments based on the pictures attached, and advertising that we are beginning to kick off our new leasing season. These apartments are ready to be rented, and we are looking to advertise these apartments to Harrowfield College college students looking for apartments.
Updates

Project Deadline Extended
Reason: I would like to see fun design elements incorporated into the flyer. Big, bold print and pictures are the main attraction

Target Market(s)

College students

Industry/Entity Type

Real Estate

Font styles to use
Sans Serif

Colors
abd037
6b449b

Requirements
Must have
• Bright colors, big bold print, pictures of college apartments
Nice to have
• I would like to see multiple pictures with BIG print
Should not have
• Animated pictures

```html
<!DOCTYPE html>
<html lang="en">
<head>
<meta charset="utf-8">
<title>Apartment For Rent – RV Stewardship Partners</title>
<link rel="stylesheet" href="https://fonts.googleapis.com/css2?family=Open+Sans:wght@600;700;800&display=swap">
<style>
  :root {
    --purple-deep: #5b3a8e;
    --purple: #6b449b;
    --magenta: #a8418f;
    --label-purple: #7d52b4;
    --yellow: #f7e21c;
    --yellow-ink: #1f6fb8;
    --green: #abd037;
    --red: #e6432e;
    --blue: #2b90d6;
    --orange: #f7941d;
    --teal: #1fb6c4;
    --white: #ffffff;
    --ink: #3a3a3a;
  }
  * { margin: 0; padding: 0; box-sizing: border-box; }
  html, body { width: 855px; height: 1200px; overflow: hidden; }
  body { font-family: "Open Sans", Arial, sans-serif; background: var(--purple); }
  .flyer {
    position: relative; width: 855px; height: 1200px; overflow: hidden;
    background: linear-gradient(180deg, var(--purple-deep) 0%, var(--purple) 45%, var(--magenta) 100%);
  }
  .tile { position: absolute; }
  .photo { background: linear-gradient(135deg, #d9cbb8 0%, #a27150 55%, #5e3a28 100%); }
  .photo.bright { background: linear-gradient(135deg, #f2f0ec 0%, #cfc7ba 60%, #9a8a74 100%); }
  .photo.sky { background: linear-gradient(180deg, #cfe3f3 0%, #e8e6e1 55%, #b9b2a6 100%); }
  .label {
    display: flex; align-items: center; justify-content: center; text-align: center;
    color: var(--white); font-weight: 700; line-height: 1.2; padding: 6px;
  }
  .label.purple { background: var(--label-purple); font-size: 24px; }
  .label.yellow { background: var(--yellow); color: var(--yellow-ink); font-size: 26px; }
  .label.green { background: var(--green); font-size: 24px; }
  .label.red { background: var(--red); font-size: 20px; }
  .label.blue { background: var(--blue); font-size: 21px; }
  .label.orange { background: var(--orange); font-size: 40px; }
  .label.red.wide { font-size: 23px; }
  .label.small { font-size: 20px; }
  .banner { position: absolute; left: 0; top: 0; }
  .headline {
    position: absolute; left: 400px; top: 935px; width: 440px;
    color: var(--white); font-weight: 800; font-size: 58px; line-height: 1.08; text-align: center;
  }
  .brand {
    position: absolute; left: 22px; top: 894px; width: 241px; height: 176px;
    background: var(--white); padding: 18px; display: flex; flex-direction: column; justify-content: flex-end;
  }
  .brand-name { color: var(--ink); font-weight: 600; font-size: 17px; line-height: 1.2; }
  .brand-mark { width: 48px; height: 48px; background: var(--purple); margin-bottom: auto; }
</style>
</head>
<body>
<main class="flyer">
  <div class="tile photo sky" style="left:22px;top:64px;width:241px;height:191px" role="img" aria-label="Photo of a large rooftop deck"></div>
  <div class="tile label purple" style="left:273px;top:64px;width:285px;height:97px">Large rooftop decks</div>
  <div class="tile photo" style="left:567px;top:64px;width:267px;height:194px" role="img" aria-label="Photo of a kitchen with red cabinets and granite counters"></div>
  <div class="tile photo bright" style="left:273px;top:167px;width:139px;height:170px" role="img" aria-label="Photo of a closet with shelving"></div>
  <div class="tile label yellow" style="left:422px;top:167px;width:136px;height:91px">Big Kitchen</div>
  <div class="tile photo" style="left:22px;top:264px;width:241px;height:190px" role="img" aria-label="Photo of a kitchen with a spiral staircase"></div>
  <div class="tile photo bright" style="left:422px;top:267px;width:294px;height:187px" role="img" aria-label="Photo of an open kitchen and living area with ceiling fan"></div>
  <div class="tile label green" style="left:273px;top:343px;width:139px;height:111px">Closets</div>
  <div class="tile label red" style="left:722px;top:267px;width:112px;height:187px">Surround sound living room</div>
  <div class="tile label blue" style="left:22px;top:463px;width:241px;height:190px">Granite countertops Hardwood floors</div>
  <div class="tile photo bright" style="left:273px;top:463px;width:294px;height:190px" role="img" aria-label="Photo of a hallway and living room with a flat screen TV"></div>
  <div class="tile label red wide" style="left:574px;top:463px;width:260px;height:190px">Living rooms with 50 inch flat screen TVs</div>
  <div class="tile photo bright" style="left:22px;top:665px;width:241px;height:199px" role="img" aria-label="Photo of a bedroom with ceiling fan"></div>
  <div class="tile label orange" style="left:273px;top:665px;width:285px;height:199px">Spacious Bedroom</div>
  <div class="tile photo" style="left:567px;top:665px;width:131px;height:199px" role="img" aria-label="Photo of a private bathroom"></div>
  <div class="tile label green small" style="left:707px;top:665px;width:127px;height:199px">Private Bathroom</div>

  <svg class="banner" width="855" height="1200" viewBox="0 0 855 1200" aria-hidden="true">
    <polygon points="285,1000 855,879 855,1118" fill="var(--teal)"/>
  </svg>
  <div class="headline">APARTMENT FOR RENT</div>

  <div class="brand">
    <div class="brand-mark"></div>
    <div class="brand-name">RV Stewardship Partners</div>
  </div>
</main>
</body>
</html>
```